Harbour Vale Lettings Web Site Design

I am after a very simple 3 page web site please. I attach a PDF with the text and information. The logo is also in the PDF. The colours should be orange and blues. The pages should be HOME - LANDLORDS - TENANTS.
Lettings and Property Management Company aimed at just being a reference point for tenants but more of a sales pitch to landlords. Please refer to the attached PDF and word file which contains far more content for the various pages.

Target Market(s)

Prospective Landlords mainly but tenants also

Industry/Entity Type

Lettings and Property Management

Number of Pages Required

3 page

Font styles to use
Sans Serif
Other font styles liked:
• Candara

Colors
0054AA
0677BA
7BADD7
CADEEF
E8F1F8
F0912C
F2A743
F7CA91
FBE8D2
FDF5EE

Requirements
Must have
• Must be colour co-ordinated to the logo (orange and dark blue predominently, Must have good quality stock images relating to property and renting out property. Should have home page and links to landlord page and tenant page. Must have the 4 logos that we are affiliated to (TKR, Tenancy Settle, BNF and Funds Guard Scheme) - all attached.
Nice to have
• Modern feel, crisp and sharp but simple - good stock images.

```html
<!DOCTYPE html>
<html lang="en">
<head>
<meta charset="utf-8">
<title>Harbour Vale Lettings</title>
<link href="https://fonts.googleapis.com/css2?family=Cinzel:wght@500;600;700&family=Outfit:wght@300;400;500&display=swap" rel="stylesheet">
<style>
:root{
  --orange:#e88a1a;
  --blue:#0ea5cf;
  --navy:#1b3163;
  --ink:#1e1e1e;
  --grey-band:#f2f2f2;
  --white:#ffffff;
}
*{margin:0;padding:0;box-sizing:border-box}
html,body{width:701px;height:1200px;overflow:hidden}
body{position:relative;background:var(--white);font-family:'Outfit',sans-serif;color:var(--ink)}
.abs{position:absolute}
.display{font-family:'Cinzel',serif;font-variant:small-caps}
.btn{position:absolute;display:flex;align-items:center;justify-content:center;border-radius:14px;color:var(--white);font-size:7.2px;font-weight:500;letter-spacing:.2px}
.btn-orange{background:var(--orange)}
.btn-blue{background:var(--blue)}

/* header */
.site-header{left:0;top:0;width:701px;height:67px;background:var(--white)}
.nav-link{top:27px;font-size:8px;font-weight:500;color:#111}
.brand-tab{left:288px;top:40px;width:126px;height:46px;background:var(--white);border-radius:0 0 14px 14px;z-index:3}
.brand{left:288px;top:10px;width:126px;text-align:center;z-index:4;color:var(--navy);font-family:'Cinzel',serif;font-weight:600}
.brand-mark{width:22px;height:22px;border-radius:50%;background:var(--orange);margin:0 auto 8px}
.brand-name{font-size:10.5px;line-height:11px}

/* hero */
.hero{left:0;top:67px;width:701px;height:309px;background:linear-gradient(100deg,#2a2a26 0%,#4b4a42 40%,#7d7f78 65%,#56606c 100%)}
.hero-title{left:82px;top:148px;font-size:22.5px;line-height:25px;color:var(--white);font-weight:500}
.hero-copy{left:82px;top:203px;width:270px;font-size:9.4px;line-height:16.5px;color:var(--white)}
.scroll-ring{left:327px;top:353px;width:46px;height:46px;border-radius:50%;background:var(--white);box-shadow:0 2px 6px rgba(0,0,0,.12);display:flex;align-items:center;justify-content:center}

/* about */
.about-arc{left:76px;top:430px;width:256px;height:256px;border-radius:50%;background:var(--blue)}
.about-photo{left:84px;top:430px;width:249px;height:249px;border-radius:50%;background:radial-gradient(circle at 60% 40%,#d9dcd6 0%,#b8b3a8 45%,#8a7663 100%)}
.eyebrow{font-size:10.5px;letter-spacing:1.6px;color:var(--blue);font-weight:500}
.section-title{font-size:19.5px;color:#111;font-weight:600}
.about-copy{left:361px;top:479px;width:256px;font-size:7.2px;line-height:12.7px;color:#222}
.about-copy p{margin-bottom:6px}
.dot-grid{left:563px;top:653px;width:85px;height:50px;background-image:radial-gradient(circle,#c9c9c9 0.8px,transparent 1px);background-size:6.3px 6.3px}

/* members */
.members{left:0;top:739px;width:701px;height:227px;background:var(--grey-band)}
.member-card{top:839px;width:125px;height:73px;background:var(--white);border-radius:4px;box-shadow:0 4px 10px rgba(0,0,0,.05);display:flex;align-items:center;justify-content:center;gap:6px;font-size:11px;color:#555}
.member-card.active{border:1px solid var(--blue)}
.badge{width:52px;height:54px;border-radius:4px}

/* footer */
.site-footer{left:0;top:966px;width:701px;height:234px;background:var(--navy)}
.on-navy{color:var(--white)}
.foot-head{top:1001px;font-size:11px;font-weight:500;color:var(--white)}
.foot-rule{top:1021px;width:19px;height:1.5px;background:var(--orange)}
.foot-links{left:83px;top:1033px;font-size:7.8px;line-height:17.2px;list-style:none;color:var(--white)}
.contact-item{font-size:7.2px;line-height:11px;color:var(--white)}
.contact-item b{font-weight:500;font-size:7.5px;display:block}
.contact-icon{left:206px}
.social{left:378px;font-size:7.2px;display:flex;align-items:center;gap:6px;color:var(--white)}
.social-dot{width:16px;height:16px;border-radius:50%;border:1px solid rgba(255,255,255,.7)}
.social-dot.on{background:var(--blue);border-color:var(--blue)}
.foot-brand{left:493px;top:1018px;width:126px;text-align:center;font-family:'Cinzel',serif;font-weight:600;font-size:15px;line-height:17px;color:var(--white)}
.foot-brand .brand-mark{width:30px;height:30px;margin-bottom:10px}
.foot-divider{left:82px;top:1167px;width:537px;height:1px;background:rgba(255,255,255,.2)}
.copyright{left:0;top:1177px;width:701px;text-align:center;font-size:7.3px;color:var(--white)}
</style>
</head>
<body>

<header class="abs site-header">
  <span class="abs nav-link" style="left:154px">HOME</span>
  <span class="abs nav-link" style="left:208px">LANDLORDS</span>
  <span class="abs nav-link" style="left:443px">TENANTS</span>
  <span class="btn btn-orange" style="left:507px;top:20px;width:112px;height:27px">LANDLORD ENQUIRY</span>
</header>
<div class="abs brand-tab"></div>
<div class="abs brand">
  <div class="brand-mark"></div>
  <div class="brand-name">HARBOUR VALE<br>LETTINGS</div>
</div>

<section class="abs hero" role="img" aria-label="Photo of a letting agent going over a rental agreement on a laptop with a young couple at a kitchen table"></section>
<h1 class="abs display hero-title">Innovative &amp; Fresh<br>Property Management</h1>
<p class="abs hero-copy">Family-run lettings agency with over 20 years of experience, offering professional services for landlords and tenants in Eastbourne and surrounding areas.</p>
<span class="btn btn-orange" style="left:82px;top:264px;width:87px;height:27px">OUR SERVICES</span>
<span class="btn btn-blue" style="left:178px;top:264px;width:87px;height:27px">CONTACT US</span>
<div class="abs scroll-ring">
  <svg width="10" height="10" viewBox="0 0 10 10"><path d="M2 1.5 5 4.5 8 1.5M2 5 5 8 8 5" fill="none" stroke="#222" stroke-width="1.1"/></svg>
</div>

<div class="abs about-arc"></div>
<div class="abs about-photo" role="img" aria-label="Photo of a hand passing house keys on a keyring over a clipboard contract"></div>
<div class="abs eyebrow" style="left:361px;top:435px">WHO WE ARE</div>
<h2 class="abs display section-title" style="left:361px;top:449px">Harbour Vale Lettings</h2>
<div class="abs about-copy">
  <p>Harbour Vale Lettings has emerged after over 20 years of privately managing our own rental properties. We are family run and decided to move all of our properties under one ‘umbrella’. Now professionally set up as a legal entity, Harbour Vale is looking to welcome new tenants and landlords to an innovative and fresh way of letting property.</p>
  <p>We always maintain a high standard of service and our friendly and helpful team are experienced in all areas and offer an excellent service in helping landlords and tenants deal with problems and<br>issues they face daily</p>
  <p>Out of hours emergency service which means we are there<br>(in an emergency) for our tenants and landlords 24/7.</p>
</div>
<span class="btn btn-orange" style="left:361px;top:642px;width:87px;height:27px">CONTACT US</span>
<div class="abs dot-grid"></div>

<section class="abs members"></section>
<div class="abs eyebrow" style="left:0;width:701px;text-align:center;top:788px">WE ARE PROUD MEMBERS OF</div>
<h2 class="abs display section-title" style="left:0;width:701px;text-align:center;top:802px">We Are Members of or Affiliated To</h2>
<div class="abs member-card" style="left:82px"><span class="badge" style="background:#7ab82f"></span>TKR</div>
<div class="abs member-card active" style="left:219px">Funds Guard Scheme</div>
<div class="abs member-card" style="left:356px">Tenancy Settle</div>
<div class="abs member-card" style="left:493px"><span class="badge" style="background:#0c2d6b;width:63px"></span>BNF</div>

<footer class="abs site-footer"></footer>
<h3 class="abs display foot-head" style="left:83px">Quick Links</h3>
<h3 class="abs display foot-head" style="left:207px">Contact Details</h3>
<h3 class="abs display foot-head" style="left:379px">Follow Us</h3>
<div class="abs foot-rule" style="left:83px"></div>
<div class="abs foot-rule" style="left:207px"></div>
<div class="abs foot-rule" style="left:379px"></div>
<ul class="abs foot-links">
  <li>• Home</li><li>• Landlords</li><li>• Tenants</li><li>• Contact Us</li>
</ul>

<svg class="abs contact-icon" style="top:1037px" width="8" height="10" viewBox="0 0 8 10"><path d="M4 0a3.5 3.5 0 0 0-3.5 3.5C.5 6 4 10 4 10s3.5-4 3.5-6.5A3.5 3.5 0 0 0 4 0z" fill="#fff"/><circle cx="4" cy="3.5" r="1.3" fill="#1b3163"/></svg>
<div class="abs contact-item" style="left:220px;top:1035px"><b>ADDRESS</b>123 Ut wisi enim ad minim<br>veniam quis nostrud.</div>
<svg class="abs contact-icon" style="top:1078px" width="8" height="8" viewBox="0 0 8 8"><path d="M1.5.5 3 2.5 2.2 3.6a5 5 0 0 0 2.2 2.2L5.5 5 7.5 6.5 6.6 7.6C3.5 7.5.5 4.5.4 1.4z" fill="#fff"/></svg>
<div class="abs contact-item" style="left:220px;top:1076px"><b>PHONE</b>123 456 7890</div>
<svg class="abs contact-icon" style="top:1110px" width="9" height="7" viewBox="0 0 9 7"><rect width="9" height="7" fill="#fff"/><path d="M0 0 4.5 4 9 0" fill="none" stroke="#1b3163" stroke-width=".8"/></svg>
<div class="abs contact-item" style="left:220px;top:1107px"><b>EMAIL</b>info@harbourvalelettings.com</div>

<div class="abs social" style="top:1036px"><span class="social-dot on"></span>Chatterly</div>
<div class="abs social" style="top:1061px"><span class="social-dot"></span>Vidstream</div>
<div class="abs social" style="top:1086px"><span class="social-dot"></span>Snapgram</div>
<div class="abs social" style="top:1112px"><span class="social-dot"></span>Chirper</div>

<div class="abs foot-brand"><div class="brand-mark"></div>HARBOUR VALE<br>LETTINGS</div>

<div class="abs foot-divider"></div>
<p class="abs copyright">© 2025 Harbour Vale Lettings. All Rights Reserved.</p>

</body>
</html>
```